Electrical Engineering Business Card Design

I need a business card design for an engineering consulting company based in Orlando, FL. I have had a logo created which the files are attached. We work primarily in the theme park and entertainment market sector but do projects in all market sectors. We have been serving Central Florida since 1994 and continue to strive to serve our clients and provide outstanding designs.
Theme Park

```html
<!DOCTYPE html>
<html lang="en">
<head>
<meta charset="utf-8">
<title>Voltaris Associates, P.A. – Business Card</title>
<link href="https://fonts.googleapis.com/css2?family=Questrial&display=swap" rel="stylesheet">
<style>
  :root {
    --stage: #e9e7e4;
    --card-black: #161616;
    --card-white: #ffffff;
    --lime: #8cc63f;
    --ink: #2b2b2b;
    --ink-soft: #4a4a4a;
    --gloss: #3d3d3d;
  }
  * { box-sizing: border-box; margin: 0; padding: 0; }
  html, body { width: 1200px; height: 716px; overflow: hidden; }
  body {
    background: var(--stage);
    font-family: "Questrial", "Century Gothic", sans-serif;
    position: relative;
  }
  .card {
    position: absolute;
    width: 540px;
    height: 309px;
    top: 204px;
    border-radius: 4px;
    box-shadow: 0 10px 24px rgba(0,0,0,0.18);
    overflow: hidden;
  }
  .card--front { left: 40px; background: var(--card-black); }
  .card--back  { left: 620px; background: var(--card-white); }

  .brand { position: absolute; display: flex; flex-direction: column; }
  .brand__row { display: flex; align-items: center; gap: 10px; }
  .brand__mark { background: var(--lime); flex: none; }
  .brand__name { white-space: nowrap; }
  .brand__place { letter-spacing: 0.28em; text-transform: uppercase; }

  .card--front .brand { left: 50%; top: 50%; transform: translate(-50%, -50%); align-items: center; }
  .card--front .brand__mark { width: 26px; height: 26px; }
  .card--front .brand__name { font-size: 30px; color: var(--gloss); }
  .card--front .brand__place { font-size: 12px; color: var(--gloss); margin-top: 6px; }

  .card--back .brand { left: 30px; top: 34px; }
  .card--back .brand__mark { width: 18px; height: 18px; }
  .card--back .brand__name { font-size: 20px; color: var(--ink); }
  .card--back .brand__place { font-size: 9px; color: var(--ink); margin-top: 4px; margin-left: 28px; }

  .address { position: absolute; left: 30px; top: 150px; font-size: 13px; line-height: 1.45; color: var(--ink-soft); }
  .address__company { color: var(--ink); font-weight: 700; }

  .contact { position: absolute; left: 300px; top: 140px; }
  .contact__name { font-size: 21px; color: var(--lime); margin-bottom: 16px; }
  .contact__list { display: grid; grid-template-columns: 58px auto; row-gap: 5px; font-size: 13px; }
  .contact__label { color: var(--lime); font-weight: 700; font-size: 12px; }
  .contact__value { color: var(--ink-soft); }

  .band { position: absolute; bottom: 0; left: 0; width: 540px; height: 16px; }
</style>
</head>
<body>
  <section class="card card--front" aria-label="Card front">
    <div class="brand">
      <div class="brand__row">
        <span class="brand__mark"></span>
        <span class="brand__name">Voltaris Associates, P.A.</span>
      </div>
      <span class="brand__place">Orlando, Florida</span>
    </div>
  </section>

  <section class="card card--back" aria-label="Card back">
    <div class="brand">
      <div class="brand__row">
        <span class="brand__mark"></span>
        <span class="brand__name">Voltaris Associates, P.A.</span>
      </div>
      <span class="brand__place">Orlando, Florida</span>
    </div>

    <address class="address" style="font-style:normal">
      <div class="address__company">Voltaris Associates, PA</div>
      <div>PO Box 410287</div>
      <div>Orlando, FL 32801</div>
    </address>

    <div class="contact">
      <div class="contact__name">Dana Whitfield</div>
      <div class="contact__list">
        <span class="contact__label">PHONE</span><span class="contact__value">407-555-0148</span>
        <span class="contact__label">FAX</span><span class="contact__value">407-555-0173</span>
        <span class="contact__label">EMAIL</span><span class="contact__value">dana.whitfield@example.com</span>
      </div>
    </div>

    <svg class="band" viewBox="0 0 540 16" aria-hidden="true">
      <rect x="0" y="6" width="230" height="10" fill="var(--lime)"/>
      <rect x="236" y="6" width="304" height="10" fill="var(--lime)"/>
    </svg>
  </section>
</body>
</html>
```